Trucking Company Website Design

We are working with a Trucking company in California. They provide trucking services for dirt, gravel, landscape bark, and landscape materials.

As you might imagine, there are no websites we could find for inspiration for trucking companies.

Thank you for taking the time to consider designing a website for us. We are web developers based in Stockton, CA, USA. Most of our projects go through the same process. Understanding this process may help you win a project with us. We custom-code all of our websites in-house. We don’t have any requirements as to what tools you use for your design, but we ask that you follow these guidelines.

IMAGES:
If you use any images or icons in the design, we ask that you have a link to the asset so we can purchase the image/icon. Most of the designs we submit do not have the customer’s images on them unless they have some great images. Be creative; show us the feeling you are trying to portray with your image choices. Use any royalty-free site you choose. We subscribe to Velmora and mainly use their images, but we can purchase images outside of Velmora. PLEASE NOTE: we will not submit designs to clients with watermarks on the images.

FONTS:
We ask that you identify the fonts you’re using in the design. This can be done in a message if you want. We typically use Pindrel Fonts and Velmora Fonts.

CONTENT:
We're always open to different content and ideas. We often submit designs with stock images so the client can see our vision. We typically take pictures after the website launch to use their images with our vision. Lorem Ipsum is fine for paragraphs, but we ask that you make the Headers with correct English. We want to be able to show the vision and identify the sections of the website.

INSPIRATION:
We typically add a couple of links in the brief of websites we like to help you get started in your design.

REVISIONS:
We do not often ask for revisions of the designs unless we see something in the design that may not appeal to the client. If there are slight changes that we want to make, we do that in the development process.

FEEDBACK:
We rarely give feedback on designs during the design process. We are working on many website projects and do not have the time to provide feedback. We usually respond if your request is well thought out and asks specific questions, but a note asking “feedback, please” usually goes unanswered.

```html
<!DOCTYPE html>
<html lang="en">
<head>
<meta charset="utf-8">
<title>Ridgeline Aggregates</title>
<link rel="stylesheet" href="https://fonts.googleapis.com/css2?family=Rajdhani:wght@600;700&family=Roboto:wght@400;500&display=swap">
<style>
:root{
  --blue:#1a7bb8;
  --blue-deep:#136aa3;
  --red:#ec1c3a;
  --red-dark:#b5122a;
  --ink:#222;
  --text:#555;
  --footer:#3b3b3b;
  --light:#f1f3f5;
}
*{margin:0;padding:0;box-sizing:border-box}
html,body{width:1200px;height:3850px;overflow:hidden;background:#fff}
body{position:relative;font-family:"Roboto",Arial,sans-serif;color:var(--text)}
.abs{position:absolute}
.head-font{font-family:"Rajdhani","Arial Narrow",sans-serif;font-weight:700}

/* header */
.brand{position:absolute;display:flex;align-items:center;gap:12px}
.brand-name{font-family:"Rajdhani",sans-serif;font-weight:700;color:var(--blue);line-height:.9;letter-spacing:1px}
.brand-mark{background:var(--red)}
.call{left:737px;top:28px;display:flex;align-items:center;gap:10px}
.call-icon{width:32px;height:32px;border-radius:50%;background:var(--red);display:flex;align-items:center;justify-content:center}
.call-text{font-family:"Rajdhani",sans-serif;font-weight:700;color:var(--blue);font-size:17px;line-height:1}
.nav{top:90px;left:0;width:1200px;height:26px}
.nav a{position:absolute;font-family:"Rajdhani",sans-serif;font-weight:700;font-size:20px;color:var(--ink);text-decoration:none}
.nav a.active{color:var(--red)}

/* buttons */
.btn{position:absolute;display:flex;align-items:center}
.btn-body{background:var(--blue);color:#fff;font-family:"Rajdhani",sans-serif;font-weight:700;font-size:17px;height:100%;display:flex;align-items:center;padding:0 22px 0 26px;border-radius:22px 0 0 22px;letter-spacing:.5px}

/* hero */
.hero{left:0;top:137px;width:1200px;height:635px;background:linear-gradient(160deg,#2a5fb0 0%,#5b8fd6 35%,#b9c2cc 62%,#8f8a80 100%)}
.hero-title{left:148px;top:258px;color:#fff;font-family:"Rajdhani",sans-serif;font-weight:700;font-size:56px;line-height:.95}
.hero-arrow{top:418px;width:74px;height:74px;border-radius:50%;display:flex;align-items:center;justify-content:center}

/* service cards */
.card{position:absolute;top:804px;width:365px;height:251px;display:flex;align-items:center;justify-content:center}
.card span{font-family:"Rajdhani",sans-serif;font-weight:700;font-size:22px;color:#fff;letter-spacing:.5px;position:relative}
.card svg.tip{position:absolute;right:10px;bottom:10px}

/* about */
.section-title{font-family:"Rajdhani",sans-serif;font-weight:700;font-size:38px;color:var(--blue)}
.section-title em{font-style:normal;color:var(--red)}
.body-copy{font-size:14px;line-height:21.6px}

/* works */
.work-img{position:absolute;top:2497px;width:292px;height:241px}
.work-cap{position:absolute;top:2758px;width:292px;text-align:center;font-family:"Rajdhani",sans-serif;font-weight:700;font-size:21px;color:var(--ink);line-height:26px}

/* contact */
.field{position:absolute;background:#fff;border:1px solid #d8d8d8;font-size:15px;color:#444;padding:15px 18px;display:flex;gap:6px;align-items:flex-start}

/* footer */
.foot-head{position:absolute;top:3515px;font-family:"Rajdhani",sans-serif;font-weight:700;font-size:19px;color:var(--red)}
.foot-list{position:absolute;top:3560px;list-style:none;font-size:14px;color:#ddd}
.foot-list li{height:26.5px}
.contact-row{position:absolute;left:781px;display:flex;gap:14px;font-size:14px;color:#ddd;line-height:21px}
.contact-ico{width:36px;height:36px;background:var(--red);display:flex;align-items:center;justify-content:center;flex:none}
</style>
</head>
<body>

<!-- header -->
<header>
  <div class="brand" style="left:128px;top:40px">
    <div class="brand-name" style="font-size:38px">RIDGELINE<br>AGGREGATES</div>
    <div class="brand-mark" style="width:26px;height:26px"></div>
  </div>
  <div class="abs call">
    <div class="call-icon"><svg width="16" height="16" viewBox="0 0 24 24"><path fill="#fff" d="M6.6 10.8a15 15 0 0 0 6.6 6.6l2.2-2.2c.3-.3.7-.4 1-.2 1.1.4 2.3.6 3.6.6.6 0 1 .4 1 1V20c0 .6-.4 1-1 1A17 17 0 0 1 3 4c0-.6.4-1 1-1h3.5c.6 0 1 .4 1 1 0 1.3.2 2.5.6 3.6.1.3 0 .7-.2 1z"/></svg></div>
    <div class="call-text">CALL:<br>555 014 2280</div>
  </div>
  <div class="btn" style="left:903px;top:22px;height:44px">
    <div class="btn-body" style="font-size:17px">GET A QUOTE</div>
    <svg width="34" height="44" viewBox="0 0 34 44"><polygon points="0,0 14,0 34,22 14,44 0,44" fill="var(--red)"/><polygon points="14,44 34,22 24,44" fill="var(--red-dark)"/></svg>
  </div>
  <nav class="abs nav">
    <a class="active" style="left:545px">HOME</a>
    <a style="left:652px">SERVICES</a>
    <a style="left:789px">ABOUT</a>
    <a style="left:894px">NEWS</a>
    <a style="left:993px">CONTACT</a>
  </nav>
</header>

<!-- hero -->
<section class="abs hero" role="img" aria-label="Yellow wheel loader pouring gravel onto a stockpile under a blue sky"></section>
<div class="abs hero-title">RIDGELINE<br>AGGREGATES</div>
<div class="abs hero-arrow" style="left:32px;background:#243a55"><svg width="22" height="22" viewBox="0 0 24 24"><path d="M15 4 7 12l8 8" stroke="#fff" stroke-width="3" fill="none"/></svg></div>
<div class="abs hero-arrow" style="left:1098px"><svg width="22" height="22" viewBox="0 0 24 24"><path d="M9 4l8 8-8 8" stroke="#fff" stroke-width="3" fill="none"/></svg></div>

<!-- service cards -->
<div class="card" style="left:28px;background:linear-gradient(180deg,#8a7e62,#6f6c66 60%,#8b8985)" role="img" aria-label="Gravel piles beneath a conveyor plant">
  <span>DIRT AND GRAVEL</span>
  <svg class="tip" width="26" height="30" viewBox="0 0 26 30"><polygon points="0,0 12,0 26,15 12,30 0,30 10,15" fill="var(--red)"/></svg>
</div>
<div class="card" style="left:419px;background:linear-gradient(180deg,#4f4a3a,#5b3326 60%,#3e2a22)" role="img" aria-label="Landscape bark mulch being spread in a garden bed">
  <span>LANDSCAPE BARK</span>
  <svg class="tip" width="26" height="30" viewBox="0 0 26 30"><polygon points="0,0 12,0 26,15 12,30 0,30 10,15" fill="var(--red)"/></svg>
</div>
<div class="card" style="left:806px;background:linear-gradient(135deg,#5e5e5e,#7f7a70 50%,#4f7a2e)" role="img" aria-label="Gravel, river rock and turf samples">
  <span>LANDSCAPE MATERIALS</span>
  <svg class="tip" width="26" height="30" viewBox="0 0 26 30"><polygon points="0,0 12,0 26,15 12,30 0,30 10,15" fill="var(--red)"/></svg>
</div>

<!-- about -->
<section>
  <div class="abs" style="left:716px;top:1174px;width:484px;height:471px;background:var(--light)"></div>
  <div class="abs" style="left:563px;top:1219px;width:505px;height:382px;background:linear-gradient(180deg,#5f8fd0 0%,#b8c6d6 40%,#a58c74 70%,#9a8b78 100%);box-shadow:0 6px 18px rgba(0,0,0,.18)" role="img" aria-label="Excavator loading a dump truck at a quarry"></div>
  <h2 class="abs section-title" style="left:128px;top:1252px">ABOUT <em>US</em></h2>
  <p class="abs body-copy" style="left:128px;top:1311px;width:370px">Lorem ipsum dolor sit amet, consectetur adipiscing elit, sed do eiusmod tempor incididunt ut labore et dolore magna aliqua. Quis ipsum suspendisse ultrices gravida. Risus commodo viverra maecenas accumsan lacus vel facilisisLorem ipsum dolor sit amet, consect etur adipiscing elit, sed do eiusmod tempor incididunt ut labore et dolore magna aliqua. Quis ipsum suspend isse ultrices gravida. Risus commodo viverra maece nas accumsan lacus vel facilisis. .</p>
  <div class="btn" style="left:130px;top:1518px;height:45px">
    <div class="btn-body">READ MORE</div>
    <svg width="38" height="45" viewBox="0 0 38 45"><polygon points="0,0 18,0 38,22.5 18,45 0,45" fill="var(--red)"/><polygon points="18,45 38,22.5 28,45" fill="var(--red-dark)"/></svg>
  </div>
</section>

<!-- why choose us -->
<section>
  <div class="abs" style="left:0;top:1740px;width:1200px;height:520px;background:linear-gradient(100deg,#5a7a3a 0%,#9fb0bf 30%,#6b7b5a 55%)" role="img" aria-label="Semi truck driving on a rural highway at sunrise"></div>
  <svg class="abs" style="left:0;top:1740px" width="1200" height="520" viewBox="0 0 1200 520">
    <polygon points="488,0 1200,0 1200,520 488,520 640,260" fill="var(--red)"/>
  </svg>
  <h2 class="abs head-font" style="left:709px;top:1853px;font-size:38px;color:#fff">WHY CHOOSE US?</h2>
  <p class="abs body-copy" style="left:709px;top:1909px;width:370px;color:#fff">Lorem ipsum dolor sit amet, consectetur adipiscing elit, sed do eiusmod tempor incididunt ut labore et dolore magna aliqua. Quis ipsum suspendisse ultrices gravida. Risus commodo viverra maecenas accumsan lacus vel facilisisLorem ipsum dolor sit amet, consect etur adipiscing elit, sed do eiusmod tempor incididunt ut labore et dolore magna aliqua.</p>
  <div class="btn" style="left:711px;top:2083px;height:45px">
    <div class="btn-body">READ MORE</div>
    <svg width="38" height="45" viewBox="0 0 38 45"><polygon points="0,0 18,0 38,22.5 18,45 0,45" fill="#fff"/><polygon points="0,2 16,2 34,22.5 16,43 0,43" fill="var(--red)"/></svg>
  </div>
</section>

<!-- latest works -->
<section>
  <h2 class="abs section-title" style="left:0;top:2350px;width:1200px;text-align:center">LATEST <em>WORKS</em></h2>
  <p class="abs body-copy" style="left:320px;top:2407px;width:560px;text-align:center;color:#777">Lorem ipsum dolor sit amet, consectetur adipiscing elit, sed do eiusmod tempor incididunt ut labore et dolore magna aliqua. Quis ipsum suspendisse ultrice</p>
  <div class="work-img" style="left:128px;background:linear-gradient(180deg,#3a6cc4,#d8cbb2 50%,#b7ab98)" role="img" aria-label="Dump truck beside a sand pile with a loader"></div>
  <div class="work-img" style="left:454px;background:linear-gradient(180deg,#6d98d4,#b89a7c 55%,#8a7d6e)" role="img" aria-label="Excavator loading a dump truck"></div>
  <div class="work-img" style="left:780px;background:linear-gradient(180deg,#6f8f5a,#c7a53c 45%,#4c3d2c)" role="img" aria-label="Compact track loader moving soil"></div>
  <div class="work-cap" style="left:128px">Lorem ipsum dolor sit amet<br>consectetur adipiscing</div>
  <div class="work-cap" style="left:454px">Lorem ipsum dolor sit amet<br>consectetur adipiscing</div>
  <div class="work-cap" style="left:780px">Lorem ipsum dolor sit amet<br>consectetur adipiscing</div>
</section>

<!-- get in touch -->
<section>
  <div class="abs" style="left:0;top:2936px;width:1200px;height:497px;background:var(--blue)" role="img" aria-label="Faint construction truck backdrop in blue"></div>
  <h2 class="abs head-font" style="left:0;top:3010px;width:1200px;text-align:center;font-size:54px;color:#fff;letter-spacing:1px">GET IN TOUCH</h2>
  <div class="field" style="left:184px;top:3106px;width:270px;height:48px">👤 Name:</div>
  <div class="field" style="left:470px;top:3106px;width:270px;height:48px">✉ Email:</div>
  <div class="field" style="left:755px;top:3106px;width:270px;height:48px">✆ Phone:</div>
  <div class="field" style="left:184px;top:3166px;width:840px;height:154px">💬 Message:</div>
  <div class="btn" style="left:518px;top:3298px;height:42px">
    <div class="btn-body" style="font-size:16px">SUBMIT NOW</div>
    <svg width="36" height="42" viewBox="0 0 36 42"><polygon points="0,0 16,0 36,21 16,42 0,42" fill="var(--red)"/><polygon points="16,42 36,21 26,42" fill="var(--red-dark)"/></svg>
  </div>
</section>

<!-- footer -->
<footer>
  <div class="abs" style="left:0;top:3433px;width:1200px;height:417px;background:var(--footer)"></div>
  <div class="brand" style="left:126px;top:3515px">
    <div class="brand-name" style="font-size:34px">RIDGELINE<br>AGGREGATES</div>
    <div class="brand-mark" style="width:22px;height:22px"></div>
  </div>
  <p class="abs" style="left:126px;top:3594px;width:240px;font-size:14px;line-height:19px;color:#ddd">Lorem ipsum dolor sit amet lore consectetur adipiscing elit, sed do eiusmod tempor incid.</p>

  <div class="foot-head" style="left:423px">HOME</div>
  <ul class="foot-list" style="left:423px"><li>About Us</li><li>Services</li><li>Projects</li><li>Meet Team</li><li>Contact Us</li></ul>

  <div class="foot-head" style="left:567px">LINKS</div>
  <ul class="foot-list" style="left:567px"><li style="height:33px">Services for Dirt</li><li style="height:33px">Gravel</li><li style="height:33px">Landscape bark</li><li>Landscape materials</li></ul>

  <div class="foot-head" style="left:781px">CONTACT</div>
  <div class="contact-row" style="top:3553px">
    <div class="contact-ico"><svg width="16" height="18" viewBox="0 0 24 24"><path fill="#fff" d="M12 2a7 7 0 0 0-7 7c0 5 7 13 7 13s7-8 7-13a7 7 0 0 0-7-7zm0 9.5A2.5 2.5 0 1 1 12 6a2.5 2.5 0 0 1 0 5.5z"/></svg></div>
    <div>Address: Local name 123<br>Street name 123 Company.</div>
  </div>
  <div class="contact-row" style="top:3618px;align-items:center">
    <div class="contact-ico"><svg width="16" height="14" viewBox="0 0 24 20"><path fill="#fff" d="M2 2h20v16H2zM3 3l9 7 9-7"/><path d="M3 3l9 7 9-7" stroke="#ec1c3a" stroke-width="2" fill="none"/></svg></div>
    <div>Email: info@ridgelineagg.com</div>
  </div>
  <div class="contact-row" style="top:3672px;align-items:center">
    <div class="contact-ico"><svg width="16" height="16" viewBox="0 0 24 24"><path fill="#fff" d="M6.6 10.8a15 15 0 0 0 6.6 6.6l2.2-2.2c.3-.3.7-.4 1-.2 1.1.4 2.3.6 3.6.6.6 0 1 .4 1 1V20c0 .6-.4 1-1 1A17 17 0 0 1 3 4c0-.6.4-1 1-1h3.5c.6 0 1 .4 1 1 0 1.3.2 2.5.6 3.6.1.3 0 .7-.2 1z"/></svg></div>
    <div>Phone: 555 014 7895</div>
  </div>

  <div class="abs" style="left:126px;top:3768px;width:946px;height:1px;background:#555"></div>
  <p class="abs" style="left:0;top:3795px;width:1200px;text-align:center;font-size:17px;color:#fff">Copyrights © 2023 All rights reserved.</p>
</footer>

</body>
</html>
```